Webdesign für Umwelt- und Vertriebsmanagement
Zielgruppe
- Umwelt- und Vertriebsmanagement
- Erarbeitung von Konzepten und Lösungen für Recyclingunternehmen
Aufgabenstellung
keine Googlemaps-Karte in das Mockup
Navigation:
- Home
- Leistungen
- Beratung
- Vertrieb
- Recycling
- Zertifikate
- Vorstellung
- Partner
- Aktuelles
- Kontakt
- Impressum / Datenschutz
in den content vorrangig die Leistungen und den Kontakt darstellen
NUR FOTOS VON 'PIXANTO' NUTZEN!

```html
<!DOCTYPE html>
<html lang="de">
<head>
<meta charset="utf-8">
<title>Verdano – Umwelt- und Vertriebsmanagement</title>
<link href="https://fonts.googleapis.com/css2?family=IBM+Plex+Sans:ital,wght@0,400;0,500;0,700;1,400&display=swap" rel="stylesheet">
<style>
:root{
  --green:#43bb35;
  --green-mark:#5de84a;
  --ink:#111;
  --text:#555;
  --muted:#777;
  --line:#ddd;
  --soft:#f7f7f7;
  --footer:#666;
  --white:#fff;
}
*{box-sizing:border-box;margin:0;padding:0}
html,body{width:827px;height:1200px;overflow:hidden;background:var(--white)}
body{font-family:"IBM Plex Sans",Arial,sans-serif;color:var(--ink)}
.page{position:relative;width:1440px;height:2090px;transform:scale(0.574306);transform-origin:0 0}
.abs{position:absolute}

/* hero */
.hero{left:0;top:0;width:1440px;height:500px;background:linear-gradient(180deg,#4d5055 0%,#6a6d70 30%,#7d6f3e 52%,#8a7a2a 70%,#5f521c 100%)}
.brand{left:120px;top:0;width:431px;height:100px;background:var(--green);color:var(--white);display:flex;align-items:center;padding-left:26px;font-weight:700}
.brand-name{font-size:34px;letter-spacing:1px;margin-right:22px}
.brand-tag{font-size:16px;line-height:23px}
.nav{left:551px;top:0;width:769px;height:100px;background:var(--white)}
.nav-main{position:absolute;left:47px;top:20px;display:flex;gap:41px;font-size:13px;font-weight:700}
.nav-sub{position:absolute;left:47px;top:67px;display:flex;gap:40px;font-size:13px;color:var(--muted)}
.nav-rule{position:absolute;left:47px;right:30px;top:52px;border-top:1px solid #e4e4e4}
.nav-icons{position:absolute;right:28px;top:18px;display:flex;gap:24px}
.hero-title{left:120px;top:172px;font-size:57px;font-weight:700;color:var(--white);letter-spacing:1px}
.hero-text{left:120px;top:250px;font-size:17px;line-height:29px;color:var(--white)}
.btn{display:flex;align-items:center;justify-content:space-between;width:170px;height:40px;padding:0 14px;font-size:15px;font-weight:700}
.btn-hero{left:120px;top:332px;border:2px solid var(--white);color:var(--white)}
.dots{left:1194px;top:433px;display:flex;gap:10px}
.dot{width:24px;height:24px;border-radius:50%;background:#000}
.dot::after{content:"";display:block;width:8px;height:8px;margin:8px;border-radius:50%;background:#999}
.dot.active{background:var(--white);border:3px solid #000}
.dot.active::after{margin:5px;background:#000}

/* services */
.card{top:530px;width:400px;height:325px;background:var(--white);border:1px solid #e6e6e6}
.card.raised{border:none;box-shadow:0 10px 30px rgba(0,0,0,.1);z-index:2}
.card-img{height:180px}
.card-body{padding:32px 44px}
.card-title{display:flex;align-items:center;gap:20px;font-size:22px;font-weight:700}
.card-desc{margin-top:10px;font-size:16px;line-height:21px;color:var(--text);width:250px}
.mark{background:linear-gradient(transparent 62%,var(--green-mark) 62%)}

/* about */
.about{left:0;top:900px;width:1440px;height:500px;background:var(--soft)}
.h1{font-size:34px;font-weight:700;letter-spacing:.5px;display:inline-block;line-height:36px}
.about-title{left:120px;top:945px}
.h2{left:120px;top:1008px;font-size:21px;font-weight:700}
.about-text{left:120px;top:1055px;width:725px;font-size:15.5px;line-height:26px;color:var(--text)}
.about-text p+p{margin-top:26px}
.more{left:120px;top:1293px;display:flex;gap:22px;align-items:center;font-size:15.5px;color:var(--text)}
.more span{text-decoration:underline}
.about-img{left:920px;top:1055px;width:400px;height:270px;background:linear-gradient(180deg,#3e4044 0%,#7b7d80 38%,#8d7c38 58%,#6b5c1f 100%)}

/* contact */
.contact-title{left:120px;top:1445px}
.label{font-size:13px;color:#222}
.field{border:1px solid #bbb;border-radius:2px;background:var(--white);height:40px;padding:0 11px;display:flex;align-items:center;font-size:13px;font-style:italic;color:#777}
.field.focus{border:2px solid var(--green);color:#222}
.btn-send{left:119px;top:1761px;border:2px solid var(--ink);color:var(--ink)}
.info{left:920px;font-size:26px;color:#666;display:flex;align-items:center;gap:22px}
.social{display:flex;gap:20px}
.social i{display:block;border-radius:50%;background:#666}

/* footer */
.footer{left:0;top:1870px;width:1440px;height:220px;background:var(--footer);color:var(--white)}
.footer-title{position:absolute;left:120px;top:34px;font-size:15px;font-weight:700}
.footer-nav{position:absolute;left:120px;top:78px;display:flex;gap:41px;font-size:13px;color:#eee}
.footer-bottom{position:absolute;left:120px;top:137px;display:flex;align-items:center;gap:20px;font-size:13px;color:#aaa}
.footer-bottom .social i{background:#ddd;width:30px;height:30px}
</style>
</head>
<body>
<div class="page">

  <div class="abs hero" role="img" aria-label="Hügelige Kornfelder unter dunklem Gewitterhimmel"></div>

  <div class="abs brand"><span class="brand-name">VERDANO</span><span class="brand-tag">UMWELT- UND<br>VERTRIEBSMANAGEMENT</span></div>

  <nav class="abs nav">
    <div class="nav-main"><span>LEISTUNGEN</span><span>BERATUNG</span><span>VERTRIEB</span><span>RECYCLING</span><span>KONTAKT</span></div>
    <div class="nav-rule"></div>
    <div class="nav-sub"><span>ZERTIFIKATE</span><span>VORSTELLUNG</span><span>PARTNER</span><span>AKTUELLES</span><span>IMPRESSUM / DATENSCHUTZ</span></div>
    <div class="nav-icons">
      <svg width="20" height="20" viewBox="0 0 20 20" fill="none" stroke="#111" stroke-width="2"><path d="M3 18V8l7-6 7 6v10z"/><path d="M8 18v-5h4v5"/></svg>
      <svg width="20" height="20" viewBox="0 0 20 20" fill="none" stroke="#111" stroke-width="2"><circle cx="8.5" cy="8.5" r="6.5"/><path d="M13.5 13.5L19 19"/></svg>
    </div>
  </nav>

  <h1 class="abs hero-title">UMWELT- UND VERTRIEBSMANAGEMENT</h1>
  <p class="abs hero-text">A short description of what’s in title, benefits, features, uniquness etc.<br>Message for a CTA technically.</p>
  <a class="abs btn btn-hero">MEHR SEHEN
    <svg width="22" height="16" viewBox="0 0 22 16" fill="none" stroke="#fff" stroke-width="2"><path d="M0 8h20M13 1l7 7-7 7"/></svg></a>
  <div class="abs dots"><span class="dot active"></span><span class="dot"></span><span class="dot"></span><span class="dot"></span></div>

  <article class="abs card" style="left:120px">
    <div class="card-img" role="img" aria-label="Hände mit Tablet und Smartphone am Schreibtisch" style="background:linear-gradient(135deg,#e8eaec,#b9bec4 55%,#6f6a66)"></div>
    <div class="card-body"><div class="card-title"><span class="mark">BERATUNG</span>
      <svg width="26" height="10" viewBox="0 0 26 10" fill="none" stroke="#111" stroke-width="1.5"><path d="M0 5h24M19 1l5 4-5 4"/></svg></div>
      <p class="card-desc">A short description of this would be nice</p></div>
  </article>
  <article class="abs card raised" style="left:520px">
    <div class="card-img" role="img" aria-label="Laptop-Tastatur mit eingeblendeten Finanzdiagrammen" style="background:linear-gradient(180deg,#c9ccd1,#7b818c 55%,#2b2f3a)"></div>
    <div class="card-body"><div class="card-title"><span class="mark">VERTRIEB</span>
      <svg width="26" height="10" viewBox="0 0 26 10" fill="none" stroke="#111" stroke-width="1.5"><path d="M0 5h24M19 1l5 4-5 4"/></svg></div>
      <p class="card-desc">A short description of this would be nice</p></div>
  </article>
  <article class="abs card" style="left:920px">
    <div class="card-img" role="img" aria-label="Industrieanlage mit Rohren und Maschinen im Gegenlicht" style="background:linear-gradient(135deg,#6d6660,#a59483 50%,#4e4a48)"></div>
    <div class="card-body"><div class="card-title"><span class="mark">RECYCLING</span>
      <svg width="26" height="10" viewBox="0 0 26 10" fill="none" stroke="#111" stroke-width="1.5"><path d="M0 5h24M19 1l5 4-5 4"/></svg></div>
      <p class="card-desc">A short description of this would be nice</p></div>
  </article>

  <section class="abs about"></section>
  <h2 class="abs about-title"><span class="h1 mark">UMWELT- UND VERTRIEBSMANAGEMENT</span></h2>
  <h3 class="abs h2">H2 TITLE</h3>
  <div class="abs about-text">
    <p>Lorem ipsum dolor sit amet, consectetur adipisicing elit, sed do eiusmod tempor incididunt ut labore et dolore magna aliqua. Ut enim ad minim veniam, quis nostrud exercitation ullamco laboris nisi ut aliquip ex ea commodo consequat.</p>
    <p>Sed ut perspiciatis unde omnis iste natus error sit voluptatem accusantium doloremque laudantium, totam rem aperiam, eaque ipsa quae ab illo inventore veritatis et quasi architecto beatae vitae dicta sunt explicabo. Nemo enim ipsam voluptatem quia voluptas sit aspernatur aut odit aut fugit, sed quia consequuntur magni dolores eos qui ratione voluptatem sequi nesciunt.</p>
  </div>
  <a class="abs more"><span>Mehr sehen</span>
    <svg width="26" height="10" viewBox="0 0 26 10" fill="none" stroke="#333" stroke-width="1.5"><path d="M0 5h24M19 1l5 4-5 4"/></svg></a>
  <div class="abs about-img" role="img" aria-label="Weites Feld mit Zypressen unter Wolkenhimmel"></div>

  <h2 class="abs contact-title"><span class="h1 mark">KONTAKT</span></h2>
  <label class="abs label" style="left:119px;top:1517px">NAME</label>
  <div class="abs field" style="left:119px;top:1539px;width:290px">Lena Berger</div>
  <label class="abs label" style="left:419px;top:1517px">EMAIL</label>
  <div class="abs field focus" style="left:419px;top:1539px;width:290px">lena.berger@mail.de</div>
  <label class="abs label" style="left:119px;top:1600px">MESSAGE</label>
  <div class="abs field" style="left:119px;top:1622px;width:590px;height:120px"></div>
  <a class="abs btn btn-send">SENDEN
    <svg width="22" height="16" viewBox="0 0 22 16" fill="none" stroke="#111" stroke-width="2"><path d="M0 8h20M13 1l7 7-7 7"/></svg></a>

  <div class="abs info" style="top:1532px">
    <svg width="24" height="26" viewBox="0 0 24 26" fill="none" stroke="#111" stroke-width="2"><rect x="6" y="2" width="12" height="22" rx="2"/></svg>
    <span>0123 456 789 00</span></div>
  <div class="abs info" style="top:1582px">
    <svg width="24" height="26" viewBox="0 0 24 26" fill="none" stroke="#111" stroke-width="2"><rect x="3" y="7" width="18" height="12" rx="2"/><path d="M3 8l9 6 9-6"/></svg>
    <span>info@verdano-beispiel.de</span></div>
  <div class="abs social" style="left:965px;top:1651px" aria-label="Soziale Netzwerke"><i style="width:38px;height:38px"></i><i style="width:38px;height:38px"></i><i style="width:38px;height:38px"></i></div>
  <div class="abs info" style="top:1723px">
    <svg width="24" height="26" viewBox="0 0 24 26" fill="none" stroke="#111" stroke-width="2"><path d="M12 24s-7-8-7-13a7 7 0 0 1 14 0c0 5-7 13-7 13z"/><circle cx="12" cy="11" r="2.5"/></svg>
    <span>City, Street XX, Office XXX</span></div>

  <footer class="abs footer">
    <div class="footer-title">UMWELT- UND VERTRIEBSMANAGEMENT</div>
    <div class="footer-nav"><span>LEISTUNGEN</span><span>BERATUNG</span><span>VERTRIEB</span><span>RECYCLING</span><span>ZERTIFIKATE</span><span>VORSTELLUNG</span><span>PARTNER</span><span>AKTUELLES</span><span>DATENSCHUTZ</span><span>KONTAKT</span></div>
    <div class="footer-bottom"><div class="social"><i></i><i></i><i></i></div><span>All rights preserved © 2019</span></div>
  </footer>

</div>
</body>
</html>
```